Design an investor pitch deck for Brindlework.io

We delivered a killer investor pitch to a group of investors last week and have been asked for a deck. we need to follow up with a killer printed version. I have produced the attached file using free images from fotovane. Feel free to change the imagery as you see fit. Check out brindlework.io to get a feel for the look and feel we have right now.

Target Market(s)

Investors

Industry/Entity Type

Software

Font styles to use
Sans Serif
Other font styles liked:
• Helvetica

Requirements
Must have
• A new version of each of the pages in the example documents. Needs to be slick and professional
Nice to have
• Other layouts in case I add further slides
Should not have
• Childish or dated shapes or designs

```html
<!DOCTYPE html>
<html lang="en">
<head>
<meta charset="utf-8">
<title>Brindlework.io – Why now?</title>
<link rel="stylesheet" href="https://fonts.googleapis.com/css2?family=Inter:wght@400;700;800&family=Roboto+Condensed:wght@700&display=swap">
<style>
  :root {
    --navy: #1f4a85;
    --purple: #5b2d87;
    --teal: #137c80;
    --sky-dots: #3fb8e6;
    --lilac-dots: #a98cc6;
    --ink: #111111;
    --frame: #333333;
    --paper: #ffffff;
  }
  * { margin: 0; padding: 0; box-sizing: border-box; }
  html, body { width: 1200px; height: 1000px; overflow: hidden; background: var(--paper); }
  body { position: relative; font-family: "Inter", Helvetica, Arial, sans-serif; color: var(--ink); }

  .slide {
    position: absolute; left: 83px; top: 280px; width: 792px; height: 447px;
    border: 1px solid var(--frame); background: var(--paper);
  }
  .slide-art { position: absolute; left: 0; top: 0; }
  .slide-title {
    position: absolute; left: 36px; top: 30px;
    font-size: 37px; font-weight: 800; color: var(--navy); letter-spacing: -0.3px;
  }
  .label {
    position: absolute; font-family: "Roboto Condensed", "Arial Narrow", sans-serif;
    font-weight: 700; text-align: center; line-height: 1.12;
    transform: translate(-50%, -50%);
  }
  .label--quote { font-size: 17px; }
  .label--pillar { font-size: 17.5px; color: var(--paper); width: 110px; }
  .navy { color: var(--navy); }
  .purple { color: var(--purple); }
  .teal { color: var(--teal); }

  .partner {
    position: absolute; transform: translate(-50%, -50%);
    font-family: "Inter", Helvetica, Arial, sans-serif; font-weight: 700; white-space: nowrap;
  }
  .partner--sm { font-size: 11px; }
  .partner--md { font-size: 15px; }

  .brand-mark {
    position: absolute; right: 18px; bottom: 16px;
    display: flex; align-items: center; gap: 6px;
    font-size: 11px; font-weight: 700; color: var(--navy);
  }
  .brand-mark .dot { width: 14px; height: 14px; border-radius: 50%; background: var(--navy); }

  .notes {
    position: absolute; left: 900px; top: 289px; width: 282px;
    font-size: 12.6px; line-height: 16.4px; color: var(--ink);
  }
  .notes strong { font-weight: 700; }
</style>
</head>
<body>

<section class="slide" aria-label="Why now slide">
  <svg class="slide-art" width="792" height="447" viewBox="0 0 792 447" aria-hidden="true">
    <!-- pillar 1 -->
    <g transform="translate(78 181)" fill="none" stroke="var(--navy)" stroke-width="1.6">
      <path d="M-17 -47 A50 50 0 0 1 35.4 35.4"/>
      <path d="M12.9 48.3 A50 50 0 0 1 -38.3 -32.1"/>
    </g>
    <circle cx="204" cy="188" r="58" fill="var(--navy)"/>
    <circle cx="175" cy="300" r="62" fill="none" stroke="var(--sky-dots)" stroke-width="2" stroke-dasharray="1.5 3.5" stroke-linecap="round"/>

    <!-- pillar 2 -->
    <g transform="translate(347 178)" fill="none" stroke="var(--purple)" stroke-width="1.6">
      <path d="M-17 -47 A50 50 0 0 1 35.4 35.4"/>
      <path d="M12.9 48.3 A50 50 0 0 1 -38.3 -32.1"/>
    </g>
    <circle cx="462" cy="182" r="58" fill="var(--purple)"/>
    <circle cx="417" cy="298" r="62" fill="none" stroke="var(--lilac-dots)" stroke-width="2" stroke-dasharray="1.5 3.5" stroke-linecap="round"/>

    <!-- pillar 3 -->
    <g transform="translate(582 176)" fill="none" stroke="var(--teal)" stroke-width="1.6">
      <path d="M-17 -47 A50 50 0 0 1 35.4 35.4"/>
      <path d="M12.9 48.3 A50 50 0 0 1 -38.3 -32.1"/>
    </g>
    <circle cx="694" cy="176" r="58" fill="var(--teal)"/>
    <circle cx="657" cy="298" r="62" fill="none" stroke="var(--sky-dots)" stroke-width="2" stroke-dasharray="1.5 3.5" stroke-linecap="round"/>

    <!-- quote marks -->
    <g font-family="Georgia, serif" font-weight="700" font-size="30">
      <text x="48" y="157" fill="var(--navy)">“</text>
      <text x="98" y="232" fill="var(--navy)">”</text>
      <text x="317" y="154" fill="var(--purple)">“</text>
      <text x="367" y="229" fill="var(--purple)">”</text>
      <text x="552" y="152" fill="var(--teal)">“</text>
      <text x="602" y="227" fill="var(--teal)">”</text>
    </g>
  </svg>

  <h1 class="slide-title">Why now?</h1>

  <div class="label label--quote navy" style="left:80px; top:181px;">Broad &amp;<br>cheap</div>
  <div class="label label--pillar" style="left:204px; top:188px;">Simple global deployment</div>

  <div class="label label--quote purple" style="left:349px; top:174px;">Modular<br>tech</div>
  <div class="label label--pillar" style="left:462px; top:182px;">Success of best-in-class integration</div>

  <div class="label label--quote teal" style="left:585px; top:164px;">Social</div>
  <div class="label label--pillar" style="left:694px; top:176px;">Shifting customer expectation</div>

  <div class="partner partner--md navy" style="left:175px; top:290px;">Cloudharbor</div>
  <div class="partner partner--sm navy" style="left:175px; top:323px;">Relaywave</div>

  <div class="partner partner--md purple" style="left:410px; top:268px;">Paystream</div>
  <div class="partner partner--md purple" style="left:420px; top:297px;">Chatterly</div>
  <div class="partner partner--sm purple" style="left:418px; top:330px;">Ledgerly</div>

  <div class="partner partner--sm teal" style="left:633px; top:274px;">Pizzaroo</div>
  <div class="partner partner--sm teal" style="left:694px; top:280px;">Ridely</div>
  <div class="partner partner--sm teal" style="left:623px; top:303px;">Marketvale</div>
  <div class="partner partner--sm teal" style="left:664px; top:336px;">Dishdash</div>

  <div class="brand-mark"><span class="dot"></span>Brindlework.io</div>
</section>

<aside class="notes">
  <p><strong>Low Cost of Deployment:</strong><br>
  smartphones are ubiquitous. Phone coverage is broad &amp; cheap. Global data centres make it fast &amp; cheap to deploy globally<br>
  <strong>Modular Tech</strong>: because there are so many great software products for specific functions, those that have a clear place, that meet that requirement beautifully, and that integrate seamlessly so that other products become their features. They win. Think Ledgerly, Chatterly, Paystream<br>
  <strong>Social:</strong> customer expectations have shifted, because in some areas of the economy companies are getting this right. You can track a $20 pizza with Pizzaroo, but you can’t track an incoming hotshot delivery. You can track a $5 felafel with Ridely Eats, but not an incoming $12,000 piece of machinery. You can continue to have your coffee meeting right up until your Ridely pulls up</p>
</aside>

</body>
</html>
```